Business Card Design Project

We're looking for a unique business card design that stands out from the rest, using the brand and logo we've already developed.
Two-sided design please.
Brightvane Media (www.brightvanemedia.com.au) is a digitally-focused advertising agency that has produces results-driven campaigns. As a result, we'd like our business card to reflect our innovative approach.
Size, shape, orientation, etc, are all flexible (providing the print costs don't become ridiculous or we have to sit there with tiny scissors!).
Business card should include space for name, title, email, mobile, landline and address.
Logo files uploaded.

```html
<!DOCTYPE html>
<html lang="en">
<head>
<meta charset="utf-8">
<title>Brightvane Media – Business Card</title>
<link rel="stylesheet" href="https://fonts.googleapis.com/css2?family=Comfortaa:wght@400;700&family=Arimo:ital,wght@0,400;0,700;1,400&display=swap">
<style>
  :root {
    --backdrop: #2b2b2b;
    --card: #0c0c0c;
    --card-edge: #1a1a1a;
    --orange: #f08a24;
    --orange-deep: #c96a12;
    --ink-light: #e8e8e8;
    --ink-soft: #b5b5b5;
    --brand-grey: #cfcfcf;
  }
  * { box-sizing: border-box; margin: 0; padding: 0; }
  html, body { width: 1200px; height: 900px; overflow: hidden; }
  body {
    background: var(--backdrop);
    font-family: "Arimo", Arial, sans-serif;
    position: relative;
  }
  .card {
    position: absolute;
    top: 170px;
    width: 330px;
    height: 560px;
    background: radial-gradient(ellipse at 50% 40%, #1a1a1a 0%, var(--card) 70%);
    border: 1px solid var(--card-edge);
    overflow: hidden;
  }
  .card--front { left: 230px; }
  .card--back  { left: 640px; }

  /* Front */
  .front-header {
    position: absolute; top: 0; left: 0; right: 0; height: 118px;
    background: #111;
  }
  .rule { position: absolute; left: 0; right: 0; height: 3px; background: var(--orange); }
  .rule--top { top: 18px; }
  .rule--bottom { top: 108px; }
  .spectrum {
    position: absolute; left: 0; right: 0; height: 3px;
    background: repeating-linear-gradient(90deg, #e23b3b 0 20px, #f0c020 20px 40px, #30b050 40px 60px, #2a8ee0 60px 80px, #a24ad0 80px 100px, #111 100px 110px);
  }
  .spectrum--top { top: 23px; }
  .spectrum--bottom { top: 113px; }
  .brand-name {
    font-family: "Comfortaa", sans-serif;
    font-weight: 700;
    color: var(--brand-grey);
  }
  .front-header .brand-name {
    position: absolute; top: 40px; left: 0; right: 0;
    text-align: center; font-size: 31px; letter-spacing: 1px;
  }
  .front-art {
    position: absolute; top: 140px; left: 30px; width: 280px; height: 300px;
    border-radius: 50%;
    background: radial-gradient(circle at 55% 45%, rgba(240,138,36,0.85) 0%, rgba(201,106,18,0.55) 45%, rgba(12,12,12,0) 72%);
  }
  .front-url {
    position: absolute; bottom: 24px; left: 0; right: 0;
    text-align: center; color: var(--ink-soft); font-size: 17px;
  }

  /* Back */
  .back-diagonal { position: absolute; inset: 0; }
  .back-diagonal svg { position: absolute; top: 0; left: 0; }
  .back-diagonal .brand-name {
    position: absolute; top: 88px; left: 106px;
    font-size: 18px; line-height: 1;
    white-space: nowrap;
    transform: translate(-50%, -50%) rotate(-39.8deg);
    transform-origin: center center;
  }
  .back-art {
    position: absolute; top: 120px; left: 110px; width: 220px; height: 220px;
    border-radius: 50%;
    background: radial-gradient(circle, rgba(120,70,25,0.55) 0%, rgba(80,45,15,0.3) 45%, rgba(12,12,12,0) 72%);
  }
  .person {
    position: absolute; top: 318px; left: 28px;
    padding-left: 20px; border-left: 5px solid var(--orange);
  }
  .person-name { color: var(--ink-light); font-size: 22px; font-weight: 400; }
  .person-title { color: var(--ink-light); font-size: 18px; margin-top: 4px; }
  .contacts { position: absolute; top: 410px; left: 32px; list-style: none; }
  .contacts li {
    display: flex; align-items: flex-start; gap: 9px;
    color: var(--ink-soft); font-size: 16px; font-style: italic;
    line-height: 1.45; margin-bottom: 2px;
  }
  .contacts svg { flex: none; width: 16px; height: 16px; margin-top: 3px; fill: var(--orange); }
</style>
</head>
<body>

<section class="card card--front" aria-label="Card front">
  <header class="front-header">
    <span class="rule rule--top"></span>
    <span class="spectrum spectrum--top"></span>
    <span class="brand-name">Brightvane Media</span>
    <span class="rule rule--bottom"></span>
    <span class="spectrum spectrum--bottom"></span>
  </header>
  <div class="front-art" role="img" aria-label="Orange swirling circular-arrow illustration with dots and ribbons"></div>
  <p class="front-url">www.brightvanemedia.com.au</p>
</section>

<section class="card card--back" aria-label="Card back">
  <div class="back-diagonal">
    <svg width="330" height="560" viewBox="0 0 330 560" aria-hidden="true">
      <line x1="0" y1="150" x2="180" y2="0" stroke="#f08a24" stroke-width="2.5"/>
      <line x1="0" y1="205" x2="245" y2="0" stroke="#f08a24" stroke-width="2.5"/>
    </svg>
    <span class="brand-name">Brightvane Media</span>
  </div>
  <div class="back-art" role="img" aria-label="Faint brown circular-arrow illustration"></div>

  <div class="person">
    <h1 class="person-name">Daniel Hart</h1>
    <p class="person-title">Director</p>
  </div>

  <ul class="contacts">
    <li>
      <svg viewBox="0 0 16 16"><path d="M4 1l3 3-2 2c1 2 3 4 5 5l2-2 3 3-2 2C7 14 2 9 2 3z"/></svg>
      0400 812 356
    </li>
    <li>
      <svg viewBox="0 0 16 16"><path d="M4 0h8v16H4zM5.5 2v10h5V2zM7 13.5h2v1H7z" fill-rule="evenodd"/></svg>
      0400 812 357
    </li>
    <li>
      <svg viewBox="0 0 16 16"><path d="M0 3h16v10H0zM1 4l7 5 7-5z" fill-rule="evenodd"/></svg>
      daniel.hart@brightvanemedia.com
    </li>
    <li>
      <svg viewBox="0 0 16 16"><path d="M8 0a5 5 0 0 1 5 5c0 4-5 11-5 11S3 9 3 5a5 5 0 0 1 5-5zm0 3a2 2 0 1 0 0 4 2 2 0 0 0 0-4z" fill-rule="evenodd"/></svg>
      42 Harbour Lane,<br>Surry Hills, Sydney
    </li>
  </ul>
</section>

</body>
</html>
```